Business card for massage therapy company called Blue Fern Wellness

Need business card for massage therapy company called Blue Fern Wellness. Would like my logo on the front and the back of the card I have 3 options of logos and you can play with what looks better.

Would like this information displayed on the back of the card:

Marcus Ellery
Licensed Massage Therapist
415-903-2264
bluefern-wellness.example
bluefern_wellness_

```html
<!DOCTYPE html>
<html lang="en">
<head>
<meta charset="utf-8">
<title>Blue Fern Wellness – Business Card</title>
<link href="https://fonts.googleapis.com/css2?family=Montserrat:wght@300;400;700&display=swap" rel="stylesheet">
<style>
  :root {
    --backdrop: #2b2b2b;
    --card-front: #1d1d1d;
    --card-back: #141414;
    --sage: #8b8d74;
    --sage-soft: rgba(139, 141, 116, 0.22);
    --copper: #b8804f;
    --ink-light: #f2f2f2;
    --silver: #a7a7a7;
  }
  * { margin: 0; padding: 0; box-sizing: border-box; }
  html, body { width: 1200px; height: 839px; overflow: hidden; }
  body {
    background: var(--backdrop);
    font-family: "Montserrat", sans-serif;
    position: relative;
  }
  .card {
    position: absolute;
    top: 87px;
    width: 380px;
    height: 665px;
    border-radius: 28px;
    overflow: hidden;
  }
  .card--front { left: 190px; background: var(--card-front); }
  .card--back  { left: 630px; background: var(--card-back); }

  .brand { position: absolute; inset: 0; }
  .brand__ring { position: absolute; left: 50%; transform: translateX(-50%); border-radius: 50%; border: 2px solid currentColor; }
  .brand__name { position: absolute; left: 0; width: 100%; text-align: center; font-weight: 300; text-transform: uppercase; line-height: 1; }
  .brand__name .line-1 { display: block; font-size: 44px; letter-spacing: 4px; }
  .brand__name .line-2 { display: block; font-size: 20px; letter-spacing: 11px; margin-top: 12px; }

  .card--front .brand { color: var(--sage); }
  .card--front .brand__ring { top: 72px; width: 140px; height: 140px; }
  .card--front .brand__name { top: 245px; }

  .card--back .brand { color: var(--silver); }
  .card--back .brand__ring { top: 150px; width: 160px; height: 160px; }
  .card--back .brand__name { top: 350px; }

  .rule { position: absolute; height: 1.6px; background: var(--sage); }
  .rule--upper { left: 96px; top: 488px; width: 228px; }
  .rule--lower { left: 106px; top: 574px; width: 232px; }

  .sprig-area { position: absolute; width: 30px; height: 52px; border-radius: 6px; background: var(--sage-soft); }
  .sprig-area--upper { left: 324px; top: 440px; }
  .sprig-area--lower { left: 338px; top: 526px; }

  .person { position: absolute; left: 36px; top: 412px; }
  .person__name { font-weight: 700; font-size: 30px; color: var(--sage); letter-spacing: 1px; text-transform: uppercase; }
  .person__role { font-weight: 400; font-size: 17px; color: var(--copper); margin-top: 4px; letter-spacing: .3px; }

  .contact { position: absolute; color: var(--ink-light); font-size: 16px; font-weight: 400; letter-spacing: .4px; }
  .contact--handle { left: 66px; top: 524px; }
  .contact--phone { left: 66px; top: 596px; }
  .contact--web { left: 66px; top: 622px; }

  .icon-dot { position: absolute; width: 28px; height: 28px; border-radius: 50%; background: var(--sage); }
  .icon-dot--social { left: 36px; top: 475px; }
  .icon-dot--phone { left: 36px; top: 560px; }
  .icon-dot--web { left: 70px; top: 560px; }
  .icon-dot svg { width: 100%; height: 100%; display: block; }
</style>
</head>
<body>

<section class="card card--front" aria-label="Card front">
  <div class="brand">
    <span class="brand__ring" aria-hidden="true"></span>
    <p class="brand__name"><span class="line-1">Blue Fern</span><span class="line-2">Wellness</span></p>
  </div>

  <span class="rule rule--upper" aria-hidden="true"></span>
  <span class="rule rule--lower" aria-hidden="true"></span>
  <div class="sprig-area sprig-area--upper" role="img" aria-label="Small leaf sprig ornament"></div>
  <div class="sprig-area sprig-area--lower" role="img" aria-label="Small leaf sprig ornament"></div>

  <div class="person">
    <p class="person__name">Marcus Ellery</p>
    <p class="person__role">Licensed Massage Therapist</p>
  </div>

  <span class="icon-dot icon-dot--social" aria-hidden="true"></span>
  <p class="contact contact--handle">bluefern_wellness_</p>

  <span class="icon-dot icon-dot--phone" aria-hidden="true">
    <svg viewBox="0 0 28 28"><path d="M10 8 l3 0 l1 4 l-2 1.5 q1.5 3 4.5 4.5 l1.5 -2 l4 1 l0 3 q-1 1.5 -3 1.5 q-6 -0.5 -10 -5 q-3.5 -4 -3.5 -7 q0 -1.5 1.5 -1.5z" fill="var(--ink-light)"/></svg>
  </span>
  <span class="icon-dot icon-dot--web" aria-hidden="true">
    <svg viewBox="0 0 28 28" fill="none" stroke="var(--ink-light)" stroke-width="1.4"><circle cx="14" cy="14" r="7"/><ellipse cx="14" cy="14" rx="3" ry="7"/><path d="M7 14 H21"/></svg>
  </span>
  <p class="contact contact--phone">415-903-2264</p>
  <p class="contact contact--web">bluefern-wellness.example</p>
</section>

<section class="card card--back" aria-label="Card back">
  <div class="brand">
    <span class="brand__ring" aria-hidden="true"></span>
    <p class="brand__name"><span class="line-1">Blue Fern</span><span class="line-2">Wellness</span></p>
  </div>
</section>

</body>
</html>
```